Design personal page for IT Expert

I'm freelancer in the area of IT Architecture/Cloud Computing/DevOps. <br/>Already have own page: www.dremtova.cc<br/><br/>I want to update/redesign it and have following sections/pages there:<br/>1) My short bio/details/soft skills<br/>2) List of my hard skills<br/>3) My key clients/success stories/feedbacks<br/>4) List of my conference talks with links/embedded youtube video<br/>5) List of my articles with links (probably article text on sub-page like blog)<br/><br/>Design should be compatible with wix.com (gona have premium plan there)<br/>

Number of Pages Required

4 page

Font styles to use
Sans Serif

Colors

Designer to choose colors to be used in the design.

Requirements
Must have
• 1) My short bio/details/soft skills
• 2) List of my hard skills
• 3) My key clients/success stories/feedbacks
• 4) List of my conference talks with links/embedded youtube video
• 5) List of my articles with links (probably article text on sub-page like blog)
Should not have
• No direct contact to my skype/email. I prefer to use this platform for my task discussion.

```html
<!DOCTYPE html>
<html lang="en">
<head>
<meta charset="utf-8">
<title>Articles/Blog – Mark Dremtov</title>
<link href="https://fonts.googleapis.com/css2?family=Playfair+Display:wght@400;700&family=Poppins:wght@300;400;500;600;700&display=swap" rel="stylesheet">
<style>
:root{
  --accent:#f47c5c;
  --accent-soft:rgba(244,124,92,.88);
  --sidebar:#2b2b2b;
  --page:#f8f8f8;
  --card:#ffffff;
  --ink:#222222;
  --muted:#9a9a9a;
  --meta:#555555;
  --line:#dddddd;
}
*{margin:0;padding:0;box-sizing:border-box}
html,body{width:962px;height:1200px;overflow:hidden}
body{background:var(--page);font-family:'Poppins',sans-serif;color:var(--ink);position:relative}

/* Sidebar */
.sidebar{position:absolute;left:0;top:0;width:189px;height:1200px;background:var(--sidebar);color:#fff;text-align:center}
.avatar{position:absolute;left:59px;top:48px;width:72px;height:72px;border-radius:50%;border:3px solid #555;background:radial-gradient(circle at 50% 45%,#c9a089,#6b5446 70%,#3a3a3a)}
.sidebar__name{position:absolute;top:135px;width:100%;font-size:11.5px;font-weight:700}
.sidebar__role{position:absolute;top:156px;width:100%;font-size:7.6px;line-height:15.5px;color:#ddd}
.sidebar__rule{position:absolute;left:36px;width:118px;height:1px;background:#3a3a3a}
.nav{position:absolute;top:250px;width:100%;list-style:none}
.nav li{font-size:9.3px;font-weight:500;height:28.3px;line-height:18px}
.nav li:first-child{height:31px}
.nav .is-active{color:var(--accent);text-decoration:underline;text-underline-offset:3px;margin-top:2px}
.connect{position:absolute;top:480px;width:100%;font-size:8px;color:#ddd}
.social{position:absolute;top:497px;left:78px;display:flex;gap:7px}
.social span{width:15px;height:15px;background:#3d3d3d;display:block}
.sidebar__foot{position:absolute;top:1178px;width:100%;font-size:6.8px;color:#777;letter-spacing:.2px}

/* Heading */
.page-title{position:absolute;left:189px;right:0;top:62px;text-align:center;font-family:'Playfair Display',serif;font-size:27px;font-weight:400;letter-spacing:.3px}
.page-title__bar{position:absolute;top:100px;left:516px;width:120px;height:1.5px;background:#e2e2e2}
.page-title__bar2{position:absolute;top:106px;left:546px;width:60px;height:1.5px;background:#e2e2e2}

/* Post cards */
.post{position:absolute;background:var(--card);box-shadow:0 1px 3px rgba(0,0,0,.04)}
.post__media{position:relative;width:100%}
.post__go{position:absolute;left:50%;bottom:-12px;margin-left:-12px;width:24px;height:24px;border-radius:50%;background:var(--accent);display:flex;align-items:center;justify-content:center}
.post__type{position:absolute;left:12px;top:12px}
.post__body{text-align:center;padding-top:20px}
.post__title{font-size:11.2px;font-weight:500;color:var(--ink)}
.post__meta{margin-top:8px;font-size:7.8px;color:var(--meta);display:flex;justify-content:center;align-items:center;gap:5px}
.post__meta i{display:inline-block;width:12px;height:1px;background:#ccc}
.post__excerpt{margin-top:10px;font-size:8.4px;font-weight:300;line-height:14.5px;color:var(--muted)}

.counts{position:absolute;top:12px;right:12px;height:21px;padding:0 6px;display:flex;align-items:center;gap:6px;background:var(--accent);color:#fff;font-size:8px;font-weight:600}
.counts span{display:flex;align-items:center;gap:3px}
.counts--outline{background:none;border:1px solid #fff}

/* Quote cards */
.quote{position:absolute;width:202px;height:301px;color:#fff;text-align:center;background:linear-gradient(160deg,#f2805f,#e9795a 55%,#dd7256)}
.quote__mark{position:absolute;left:12px;top:4px;font-family:'Playfair Display',serif;font-weight:700;font-size:52px;line-height:1}
.quote__title{position:absolute;top:95px;left:0;right:0;font-size:12.4px;font-weight:700;line-height:20.5px}
.quote__meta{position:absolute;top:146px;left:0;right:0;font-size:7.8px;display:flex;justify-content:center;align-items:center;gap:4px}
.quote__meta i{display:inline-block;width:16px;height:1px;background:#fff}
.quote__go{position:absolute;top:176px;left:89px;width:24px;height:24px;border:1.3px solid #fff;border-radius:50%;display:flex;align-items:center;justify-content:center}

/* Pager */
.pager{position:absolute;top:1096px;height:30px;display:flex;align-items:center;justify-content:center;gap:4px;font-size:8.4px;font-weight:600}
.pager--prev{left:491px;width:80px;border:1.2px solid var(--accent);color:var(--accent)}
.pager--next{left:580px;width:81px;background:var(--accent);color:#fff}
</style>
</head>
<body>

<aside class="sidebar">
  <div class="avatar" role="img" aria-label="Portrait photo of Mark Dremtov"></div>
  <div class="sidebar__name">Mark Dremtov</div>
  <div class="sidebar__role">-Nimbus Cloud DevOps &amp; Architect<br>-CI/CD Automation Expert</div>
  <div class="sidebar__rule" style="top:218px"></div>
  <ul class="nav">
    <li>HOME</li>
    <li>ABOUT ME</li>
    <li>HARD SKILLS</li>
    <li>SUCCESSFUL STORIES</li>
    <li>CONFERENCE TALKS</li>
    <li class="is-active">ARTICLES/BLOG</li>
  </ul>
  <div class="sidebar__rule" style="top:445px"></div>
  <div class="connect">Connect With Me:</div>
  <div class="social"><span></span><span></span></div>
  <div class="sidebar__foot">ALL RIGHTS RESERVED</div>
</aside>

<h1 class="page-title">Articles/Blog</h1>
<div class="page-title__bar"></div>
<div class="page-title__bar2"></div>

<svg width="0" height="0" style="position:absolute">
  <defs>
    <symbol id="i-bubble" viewBox="0 0 12 11"><path d="M6 0C2.7 0 0 2 0 4.6c0 1.4.8 2.6 2 3.4L1.4 11l3-1.9c.5.1 1 .2 1.6.2 3.3 0 6-2.1 6-4.7S9.3 0 6 0z" fill="currentColor"/></symbol>
    <symbol id="i-heart" viewBox="0 0 12 11"><path d="M6 11L1 6C-.5 4.4-.3 1.8 1.4.6 2.9-.4 4.8 0 6 1.5 7.2 0 9.1-.4 10.6.6c1.7 1.2 1.9 3.8.4 5.4z" fill="currentColor"/></symbol>
    <symbol id="i-arrow" viewBox="0 0 10 8"><path d="M0 4h9M6 1l3 3-3 3" fill="none" stroke="currentColor" stroke-width="1"/></symbol>
    <symbol id="i-screen" viewBox="0 0 24 20"><rect x="1" y="1" width="22" height="14" fill="none" stroke="currentColor" stroke-width="1.6"/><path d="M8 19h8M12 15v4" stroke="currentColor" stroke-width="1.6"/></symbol>
  </defs>
</svg>

<!-- Row 1 -->
<article class="quote" style="left:252px;top:151px">
  <div class="quote__mark">&#8221;</div>
  <div class="counts counts--outline"><span><svg width="11" height="10" style="color:#fff"><use href="#i-bubble"/></svg>20</span><span><svg width="11" height="10" style="color:#fff"><use href="#i-heart"/></svg>20</span></div>
  <div class="quote__title">Lorem Ipsumi Is Not Dolor<br>Lorem Is Amet</div>
  <div class="quote__meta">Jan17-2020 <i></i> Development</div>
  <div class="quote__go"><svg width="10" height="8" style="color:#fff"><use href="#i-arrow"/></svg></div>
</article>

<article class="post" style="left:472px;top:151px;width:427px;height:301px">
  <div class="post__media" style="height:210px;background:linear-gradient(120deg,#dcdcdc 0%,#3a3d42 35%,#1e2125 60%,#c9c3b8 100%)" role="img" aria-label="Photo of a developer with headphones coding at a monitor">
    <svg class="post__type" width="24" height="20" style="color:var(--accent)"><use href="#i-screen"/></svg>
    <div class="counts"><span><svg width="11" height="10"><use href="#i-bubble"/></svg>20</span><span><svg width="11" height="10"><use href="#i-heart"/></svg>20</span></div>
    <div class="post__go"><svg width="10" height="8" style="color:#fff"><use href="#i-arrow"/></svg></div>
  </div>
  <div class="post__body">
    <div class="post__title">The Lorem Ipsum Of Dolor</div>
    <div class="post__meta">Jan 18-2020 <i></i> Development <i></i> Tags</div>
    <div class="post__excerpt">Lorem ipsum dolor amet plaid listicle man braid, live-edge kickstarter met</div>
  </div>
</article>

<!-- Row 2 -->
<article class="post" style="left:252px;top:470px;width:203px;height:271px">
  <div class="post__media" style="height:165px;background:linear-gradient(135deg,#b58a5e,#8a7a6a 45%,#3f6f8c)" role="img" aria-label="Photo of hands typing on a laptop on a patterned desk">
    <svg class="post__type" width="24" height="20" style="color:var(--accent)"><use href="#i-screen"/></svg>
    <div class="counts"><span><svg width="11" height="10"><use href="#i-bubble"/></svg>20</span><span><svg width="11" height="10"><use href="#i-heart"/></svg>20</span></div>
    <div class="post__go"><svg width="10" height="8" style="color:#fff"><use href="#i-arrow"/></svg></div>
  </div>
  <div class="post__body">
    <div class="post__title">The Lorem Ipsum Of Dolor</div>
    <div class="post__meta">Jan 18-2020 <i></i> Development <i></i> Tags</div>
    <div class="post__excerpt">Lorem ipsum dolor amet plaid listicle<br>eiman braid, live-edge kickstarter met</div>
  </div>
</article>

<article class="post" style="left:473px;top:470px;width:203px;height:271px">
  <div class="post__media" style="height:165px;background:linear-gradient(135deg,#2a2a2a,#1a1a1a 55%,#9a9a9a)" role="img" aria-label="Photo of a laptop, watch and mouse on a dark desk">
    <svg class="post__type" width="24" height="20" style="color:var(--accent)"><use href="#i-screen"/></svg>
    <div class="counts"><span><svg width="11" height="10"><use href="#i-bubble"/></svg>20</span><span><svg width="11" height="10"><use href="#i-heart"/></svg>20</span></div>
    <div class="post__go"><svg width="10" height="8" style="color:#fff"><use href="#i-arrow"/></svg></div>
  </div>
  <div class="post__body">
    <div class="post__title">The Lorem Ipsum Of Dolor</div>
    <div class="post__meta">Jan 18-2020 <i></i> Development <i></i> Tags</div>
    <div class="post__excerpt">Lorem ipsum dolor amet plaid listicle<br>eiman braid, live-edge kickstarter met</div>
  </div>
</article>

<article class="post" style="left:694px;top:470px;width:203px;height:271px">
  <div class="post__media" style="height:165px;background:linear-gradient(135deg,#eceff2,#d9dde2 50%,#3d5a86)" role="img" aria-label="Photo of a man drawing a diagram on a whiteboard">
    <svg class="post__type" width="24" height="20" style="color:var(--accent)"><use href="#i-screen"/></svg>
    <div class="counts"><span><svg width="11" height="10"><use href="#i-bubble"/></svg>20</span><span><svg width="11" height="10"><use href="#i-heart"/></svg>20</span></div>
    <div class="post__go"><svg width="10" height="8" style="color:#fff"><use href="#i-arrow"/></svg></div>
  </div>
  <div class="post__body">
    <div class="post__title">The Lorem Ipsum Of Dolor</div>
    <div class="post__meta">Jan 18-2020 <i></i> Development <i></i> Tags</div>
    <div class="post__excerpt">Lorem ipsum dolor amet plaid listicle<br>eiman braid, live-edge kickstarter met</div>
  </div>
</article>

<!-- Row 3 -->
<article class="post" style="left:252px;top:759px;width:427px;height:301px">
  <div class="post__media" style="height:210px;background:linear-gradient(120deg,#5a4a3e,#3b3a3a 45%,#6b6258 75%,#8c8276)" role="img" aria-label="Photo of a team working on laptops around a table">
    <svg class="post__type" width="24" height="20" style="color:var(--accent)"><use href="#i-screen"/></svg>
    <div class="counts"><span><svg width="11" height="10"><use href="#i-bubble"/></svg>20</span><span><svg width="11" height="10"><use href="#i-heart"/></svg>20</span></div>
    <div class="post__go"><svg width="10" height="8" style="color:#fff"><use href="#i-arrow"/></svg></div>
  </div>
  <div class="post__body">
    <div class="post__title">The Lorem Ipsum Of Dolor</div>
    <div class="post__meta">Jan 18-2020 <i></i> Development <i></i> Tags</div>
    <div class="post__excerpt">Lorem ipsum dolor amet plaid listicle man braid, live-edge kickstarter met</div>
  </div>
</article>

<article class="quote" style="left:697px;top:759px">
  <div class="quote__mark">&#8221;</div>
  <div class="counts counts--outline"><span><svg width="11" height="10" style="color:#fff"><use href="#i-bubble"/></svg>20</span><span><svg width="11" height="10" style="color:#fff"><use href="#i-heart"/></svg>20</span></div>
  <div class="quote__title">Lorem Ipsumi Is Not Dolor<br>Lorem Is Amet</div>
  <div class="quote__meta">Jan17-2020 <i></i> Development</div>
  <div class="quote__go"><svg width="10" height="8" style="color:#fff"><use href="#i-arrow"/></svg></div>
</article>

<!-- Pagination -->
<div class="pager pager--prev"><svg width="10" height="8" style="color:var(--accent);transform:scaleX(-1)"><use href="#i-arrow"/></svg>PREV</div>
<div class="pager pager--next">NEXT<svg width="10" height="8" style="color:#fff"><use href="#i-arrow"/></svg></div>

</body>
</html>
```